Preliminary design concepts for VARELTH history document

To produce three design concepts as a demonstration for the layout of a document with a look and feel compatible with the existing documents/visual identity of an Australia-based NGO. The design concepts will be used to provide concepts to the NGO and ideally select a designer for the longer 30 - 50 page document.

Target Market(s)

Australian heritage community, international heritage community, general population interested in heritage issues and key stakeholders in heritage projects

Colors
0455a3
3176b5
85acd3
ffc214
fece3e
fee18a
f78f20
f37122

Requirements
Must have
• Eye catching but authoritative design to reflect a serious professional organisation, but one which reflects a modern, progressive approach.
• The designer needs to have experience working with document layout in InDesign and/or Illustrator and provide files in a range of outputs including EPS formats as well as HTML and PDF.
Nice to have
• Interplay between images and design elements

```html
<!DOCTYPE html>
<html lang="en">
<head>
<meta charset="utf-8">
<title>Innovation in Conservation — Cover</title>
<link href="https://fonts.googleapis.com/css2?family=Jost:wght@300;400&display=swap" rel="stylesheet">
<style>
  :root {
    --stage: #d6d6d6;
    --navy: #2b3275;
    --orange: #f58634;
    --orange-deep: #f37122;
    --paper: #ffffff;
    --ink-light: #ffffff;
  }
  html, body {
    margin: 0;
    width: 1200px;
    height: 1200px;
    overflow: hidden;
    background: var(--stage);
    font-family: "Jost", "Futura", sans-serif;
  }
  .cover {
    position: absolute;
    left: 195px;
    top: 40px;
    width: 810px;
    height: 1120px;
    background: var(--paper);
    overflow: hidden;
  }
  .spine-band {
    position: absolute;
    top: 0;
    right: 0;
    width: 130px;
    height: 100%;
    background: var(--navy);
  }
  .cover-photo {
    position: absolute;
    left: 0;
    top: 0;
    width: 680px;
    height: 640px;
    background: linear-gradient(180deg, #e4e4e4 0%, #b9b9b9 35%, #7a7a7a 65%, #5c5c5c 100%);
  }
  .title-band {
    position: absolute;
    left: 0;
    top: 640px;
    width: 680px;
    height: 320px;
    background: linear-gradient(90deg, var(--orange) 0%, var(--orange-deep) 100%);
  }
  .title-main {
    position: absolute;
    left: 28px;
    top: 588px;
    margin: 0;
    font-weight: 300;
    font-size: 100px;
    line-height: 1;
    letter-spacing: -0.01em;
    color: var(--navy);
  }
  .title-sub {
    position: absolute;
    left: 34px;
    top: 700px;
    margin: 0;
    font-weight: 300;
    font-size: 46px;
    letter-spacing: 0.22em;
    color: var(--ink-light);
  }
  .rule {
    position: absolute;
    left: 0;
    width: 680px;
    height: 2px;
    background: var(--ink-light);
  }
  .rule-upper { top: 768px; }
  .rule-lower { top: 880px; }
  .subtitle {
    position: absolute;
    right: 150px;
    top: 782px;
    margin: 0;
    width: 560px;
    text-align: right;
    font-weight: 300;
    font-size: 29px;
    line-height: 1.2;
    color: var(--ink-light);
  }
  .publisher {
    position: absolute;
    right: 150px;
    top: 990px;
    display: flex;
    align-items: center;
    gap: 12px;
    font-weight: 400;
    font-size: 22px;
    letter-spacing: 0.02em;
    color: var(--navy);
  }
  .publisher-dot {
    width: 34px;
    height: 34px;
    border-radius: 50%;
    background: var(--navy);
  }
</style>
</head>
<body>
  <main class="cover">
    <div class="cover-photo" role="img" aria-label="Black and white photograph of a ruined stone mine engine house with a tall chimney on a grassy hillside"></div>
    <div class="title-band"></div>
    <div class="spine-band"></div>

    <h1 class="title-main">INNOVATION</h1>
    <p class="title-sub">IN CONSERVATION</p>
    <div class="rule rule-upper"></div>
    <p class="subtitle">A brief history of Australia VARELTH<br>and the Kerrin Charter</p>
    <div class="rule rule-lower"></div>

    <div class="publisher">
      <span>AUSTRALIA VARELTH</span>
      <span class="publisher-dot"></span>
    </div>
  </main>
</body>
</html>
```